New Alcoholic Spiked Seltzer Line

We need a can design for a line of low calorie alcoholic seltzer. This product is a sparkling water and vodka drink with no sugar added in a slim 12 oz can.

This is a lighter, healthier, alternative to the sugary ready-to-drinks on the market. The product contains only 3 ingredients: Vodka, Water and Natural Flavors. It has only 100 calories but still has 5% alcohol, so you don't need to sacrifice alcohol to cut calories.

This product also does not contain any preservatives.

We want this design to communicate the following objectives to the consumer and in this order:

1. Appetizing product
2.Low calorie
3.Communicate the type of beverage (Spiked Seltzer)

The brand name of the product is VELKA.

The flavor of the product needed to be used for the design is Mango-Orange.

Comparable products are:

www.brisavelfizz.example/
https://www.tarnowbubble.example
https://quellrind.example/

The designs should not infringe or copy the creative directions of the products mentionned above. They are only given so that you can better understand the type of product we are developing.

Target Market(s)

Young Professional women between the ages of 25 and 44

Industry/Entity Type

Product

Colors

Designer to choose colors to be used in the design.

Requirements
Must have
• Design extendibility, meaning it can be adapted for other flavors.
• This is a new category in the market we are targeting, so consumers must easily be able to identify what type of product this is.

```html
<!DOCTYPE html>
<html lang="en">
<head>
<meta charset="utf-8">
<title>VELKA Mango Orange Spiked Seltzer – Can Label</title>
<link rel="stylesheet" href="https://fonts.googleapis.com/css2?family=Raleway:wght@300;400;800&family=Roboto+Condensed:wght@400&display=swap">
<style>
  :root {
    --page-bg: #ffffff;
    --can-silver-light: #eeeeee;
    --can-silver-mid: #dcdcdc;
    --can-silver-dark: #c4c4c4;
    --mango-orange: #ec7a22;
    --ink: #2b2b2b;
  }
  html, body {
    margin: 0;
    padding: 0;
    width: 1200px;
    height: 1200px;
    overflow: hidden;
    background: var(--page-bg);
  }
  .canvas {
    position: relative;
    width: 1200px;
    height: 1200px;
  }
  .label {
    position: absolute;
    left: 400px;
    top: 100px;
    width: 400px;
    height: 1000px;
    overflow: hidden;
    background: linear-gradient(90deg,
      var(--can-silver-dark) 0%,
      var(--can-silver-light) 22%,
      var(--can-silver-mid) 60%,
      var(--can-silver-light) 82%,
      var(--can-silver-dark) 100%);
  }
  .brand-name {
    position: absolute;
    left: -164px;
    top: 335px;
    width: 640px;
    height: 170px;
    transform: rotate(-90deg);
    margin: 0;
    font-family: "Raleway", sans-serif;
    font-weight: 800;
    font-size: 176px;
    line-height: 170px;
    letter-spacing: 6px;
    text-align: center;
    color: var(--mango-orange);
  }
  .tagline {
    position: absolute;
    left: 2px;
    top: 375px;
    width: 620px;
    height: 90px;
    transform: rotate(-90deg);
    text-align: center;
    color: var(--ink);
    font-family: "Raleway", sans-serif;
  }
  .tagline-main {
    display: block;
    font-size: 41px;
    font-weight: 300;
    line-height: 50px;
    letter-spacing: 1px;
    white-space: nowrap;
  }
  .tagline-main strong { font-weight: 800; }
  .tagline-sub {
    display: block;
    font-size: 26px;
    font-weight: 400;
    line-height: 34px;
    letter-spacing: 3px;
  }
  .flavor-band {
    position: absolute;
    left: 0;
    top: 905px;
    width: 400px;
    height: 0;
  }
  .flavor-band-pattern {
    position: absolute;
    background: var(--mango-orange);
  }
  .flavor-band-pattern.left { left: 0; top: -70px; width: 58px; height: 60px; }
  .flavor-band-pattern.right { left: 265px; top: -75px; width: 135px; height: 72px; }
  .flavor-name {
    position: absolute;
    left: 72px;
    top: -88px;
    margin: 0;
    font-family: "Raleway", sans-serif;
    font-weight: 800;
    font-size: 34px;
    line-height: 36px;
    color: var(--mango-orange);
  }
  .legal-line {
    position: absolute;
    left: 84px;
    top: 938px;
    margin: 0;
    font-family: "Roboto Condensed", sans-serif;
    font-size: 22px;
    line-height: 28px;
    color: var(--ink);
    white-space: nowrap;
  }
  .legal-line span + span { margin-left: 30px; }
</style>
</head>
<body>
  <main class="canvas">
    <section class="label">
      <h1 class="brand-name">VELKA</h1>
      <p class="tagline">
        <span class="tagline-main">100CALORIE<strong>SPIKED</strong>SELTZER</span>
        <span class="tagline-sub">WITH NATURAL FLAVORS</span>
      </p>
      <div class="flavor-band">
        <div class="flavor-band-pattern left" role="img" aria-label="Orange band with decorative flourish pattern"></div>
        <h2 class="flavor-name">MANGO<br>ORANGE</h2>
        <div class="flavor-band-pattern right" role="img" aria-label="Orange band with decorative flourish pattern"></div>
      </div>
      <p class="legal-line"><span>5% ALC/VOL</span><span>NET 12 FL OZ</span></p>
    </section>
  </main>
</body>
</html>
```